Carpet Cleaning Business Sesighn

Brightway is a carpet cleaning company we do more than carpet cleaning, carpet cleaning, upholstery cleaning, tile and grout cleaning, wood floor cleaning & refinishing, maid service, air duct cleaning, pet odor and urine removal, water restoration and carpet repair. we need a business card design for our company to match our web site http://www.brightway-carpet-cleaning.example we also need our logo on our card something like our web site, colors are red, gray, black like our web site. I want the logo to pop like our web site also.
Industry/Entity Type
Business
Contact Information for Business Card
Brightway Carpet Cleaning
Martin Oakes
1187 Larkspur Rd Millbrook, IL 60999
President
Office 555 273-9160
Cell 555 384-6017
Email Martin@Brightway-Carpet-Cleaning.example
www.brightway-carpet-cleaning.example

```html
<!DOCTYPE html>
<html lang="en">
<head>
<meta charset="utf-8">
<title>Brightway Carpet Cleaning – Business Card</title>
<link rel="stylesheet" href="https://fonts.googleapis.com/css2?family=Source+Sans+3:wght@400;600;700&display=swap">
<style>
  :root {
    --page: #ecebe8;
    --red-deep: #8f1416;
    --red-mid: #b8252a;
    --red-bright: #d3282d;
    --white: #ffffff;
    --mist: #e4e4e4;
    --gray-mark: #5f6063;
    --shadow: rgba(0, 0, 0, 0.28);
  }
  * { margin: 0; padding: 0; box-sizing: border-box; }
  html, body {
    width: 1200px; height: 900px; overflow: hidden;
    background: var(--page);
    font-family: "Source Sans 3", "Myriad Pro", Arial, sans-serif;
  }
  .canvas { position: relative; width: 1200px; height: 900px; }

  .card {
    position: absolute;
    width: 658px; height: 387px;
    background: radial-gradient(ellipse at 45% 40%, var(--red-bright) 0%, var(--red-mid) 45%, var(--red-deep) 100%);
    box-shadow: 0 4px 14px var(--shadow);
    overflow: hidden;
  }
  .card--front { left: 142px; top: 45px; }
  .card--back { left: 393px; top: 475px; width: 660px; }

  /* front */
  .front-oval { position: absolute; left: 56px; top: 44px; width: 555px; height: 262px; }
  .wordmark {
    position: absolute; display: flex; align-items: center; gap: 14px;
    font-weight: 700; color: var(--gray-mark); letter-spacing: 0.5px;
  }
  .wordmark__dot { border-radius: 50%; background: var(--red-mid); }
  .card--front .wordmark { left: 0; right: 0; top: 128px; justify-content: center; font-size: 72px; line-height: 1; }
  .card--front .wordmark__dot { width: 30px; height: 30px; }
  .front-web {
    position: absolute; left: 0; right: 0; top: 325px; text-align: center;
    color: var(--white); font-weight: 700; font-size: 25px;
  }

  /* back */
  .back-swoop { position: absolute; left: 0; top: 0; width: 660px; height: 387px; }
  .card--back .wordmark { left: 300px; top: 68px; font-size: 54px; line-height: 1; }
  .card--back .wordmark__dot { width: 24px; height: 24px; }
  .contact { position: absolute; left: 30px; top: 150px; color: var(--white); }
  .contact__name { font-weight: 700; font-size: 37px; line-height: 1.1; margin-bottom: 16px; }
  .contact__line { font-size: 21px; line-height: 30px; }
  .contact__line--gap { margin-top: 4px; }
</style>
</head>
<body>
<main class="canvas">

  <section class="card card--front" aria-label="Card front">
    <svg class="front-oval" viewBox="0 0 555 262" aria-hidden="true">
      <defs>
        <linearGradient id="ovalFill" x1="0" y1="0" x2="0" y2="1">
          <stop offset="0" stop-color="#ffffff"/>
          <stop offset="1" stop-color="#dcdcdc"/>
        </linearGradient>
      </defs>
      <ellipse cx="277.5" cy="131" rx="272" ry="126" fill="#a51b1f" stroke="#ffffff" stroke-width="5"/>
      <ellipse cx="277.5" cy="131" rx="258" ry="113" fill="url(#ovalFill)"/>
    </svg>
    <div class="wordmark"><span class="wordmark__dot"></span>Brightway</div>
    <p class="front-web">www.brightway-carpet-cleaning.example</p>
  </section>

  <section class="card card--back" aria-label="Card back">
    <svg class="back-swoop" viewBox="0 0 660 387" aria-hidden="true">
      <defs>
        <linearGradient id="swoopFill" x1="0" y1="0" x2="0" y2="1">
          <stop offset="0" stop-color="#ffffff"/>
          <stop offset="1" stop-color="#e2e2e2"/>
        </linearGradient>
      </defs>
      <path d="M214 0 C 232 150, 430 228, 660 230 L 660 0 Z" fill="#ffffff"/>
      <path d="M230 0 C 248 138, 440 212, 660 214 L 660 0 Z" fill="#a51b1f"/>
      <path d="M240 0 C 258 128, 446 202, 660 204 L 660 0 Z" fill="url(#swoopFill)"/>
    </svg>
    <div class="wordmark"><span class="wordmark__dot"></span>Brightway</div>
    <div class="contact">
      <h1 class="contact__name">Martin Oakes</h1>
      <p class="contact__line">1187 Larkspur Rd</p>
      <p class="contact__line">Millbrook, IL 60999</p>
      <p class="contact__line contact__line--gap">President Office 555 273-9160</p>
      <p class="contact__line">Cell 555 384-6017</p>
      <p class="contact__line">Email Martin@Brightway-Carpet-Cleaning.example</p>
    </div>
  </section>

</main>
</body>
</html>
```